Custom LED sign business needs logo and web design.

We need a logo and website design for a new company based in Austin TX. What we do is laser engrave custom artwork for led edge lit signs. Our marketing will be directed to kids rooms, game rooms and business. I would like to see designs that have a neon text effect. The look should feel professional for businesses and fun for kids.

**UPDATE** This website will need a custom design page that uses Fancy Product Designer type plugin. The users will be able to choose from pre-loaded artwork and fonts or upload there own artwork.
There will also be a ecommerce tab that will. have ready to ship signs available.
Wordpress will be the platform used.

Target Market(s)

Businesses, kids and game rooms

Contact Information for Business Card

Neon Text effect with logo. Professional but fun.

Logo Text

Brivaglo

Coding

Coded - Design and coding required

Number of Pages Required

5+ page

Font styles to use
Other font styles liked:
• A neon text effect type font. Example picture added

Colors

Designer to choose colors to be used in the design.

Requirements
Must have
• Neon Text effects with a professional tech look. Incorporate the "create", "energize" and "amaze" as the company slogan.
• Fancy Product Designer for customer interactive sign design.
• Ecommerce platform so that I can upload ready to ship signs.
• Refer to the Create, Energize, Amaze pics attached as company slogan. Use those fonts.
Nice to have
• I would like text to "turn on" when hovered over.
Should not have
• Scattered text locations. Unorganized layout and feel.

```html
<!DOCTYPE html>
<html lang="en">
<head>
<meta charset="utf-8">
<title>Brivaglo — LED Edge Lit Signs</title>
<link rel="stylesheet" href="https://fonts.googleapis.com/css2?family=Montserrat:wght@300;400;600;700;800&family=Open+Sans:wght@400;600;700&display=swap">
<style>
:root{
  --bg:#121212;
  --bg-dark:#0b0b0b;
  --bg-panel:#1c1c1c;
  --card:#393939;
  --card-dark:#2a2a2a;
  --orange:#ff6a1f;
  --orange-glow:#ff3d00;
  --red:#d9411e;
  --violet:#8c7dff;
  --white:#ffffff;
  --muted:#bdbdbd;
  --line:#3a3a3a;
}
*{box-sizing:border-box;margin:0;padding:0}
html,body{width:1200px;height:4206px;overflow:hidden}
body{background:var(--bg);color:var(--white);font-family:"Open Sans",Arial,sans-serif;position:relative}
.wrap{position:relative;width:940px;margin:0 auto}
.neon-heading{font-family:"Montserrat",Arial,sans-serif;font-weight:800;color:var(--orange);text-align:center;letter-spacing:2px;text-shadow:0 0 6px var(--orange-glow),0 0 18px var(--orange-glow)}
.btn{display:inline-block;background:var(--red);color:var(--white);font-family:"Montserrat",Arial,sans-serif;font-weight:700;font-size:13px;letter-spacing:.5px;padding:11px 14px;border-radius:2px;text-transform:uppercase}

/* header */
.site-header{height:140px;background:var(--bg)}
.brand{position:absolute;left:0;top:34px;font-family:"Montserrat",Arial,sans-serif;font-weight:300;font-size:58px;letter-spacing:1px;color:var(--orange);text-transform:uppercase}
.utility{position:absolute;right:0;top:30px;display:flex;align-items:center;gap:14px;font-size:11px}
.search{width:140px;height:30px;border:1px solid #555;background:#1a1a1a;display:flex;align-items:center;justify-content:space-between;padding:0 10px;color:#ccc}
.call{display:flex;align-items:center;gap:6px;line-height:1.2}
.call small{display:block;font-size:8px;color:#aaa}
.login{border:1px solid #555;padding:7px 12px;display:flex;gap:6px;align-items:center}
.cart{border:1px solid #555;padding:6px 10px;display:flex;gap:6px;align-items:center;font-weight:700;font-size:10px;position:relative}
.cart .count{position:absolute;right:-6px;top:-8px;width:16px;height:16px;border-radius:50%;background:var(--orange);font-size:9px;display:flex;align-items:center;justify-content:center}
.main-nav{position:absolute;right:0;top:96px;display:flex;gap:34px;font-family:"Montserrat",Arial,sans-serif;font-weight:700;font-size:13px}
.main-nav a{color:var(--white);text-decoration:none}
.main-nav a.active{color:var(--orange)}

/* hero */
.hero{height:555px;position:relative;background:radial-gradient(ellipse at 50% 55%,#2c2350 0%,#151433 45%,#0b0b1a 100%)}
.hero-title{position:absolute;top:60px;left:0;right:0;font-size:50px}
.hero-art{position:absolute;left:190px;top:190px;width:810px;height:335px;border-radius:20px;background:radial-gradient(ellipse at center,#3a1f6e 0%,#231c55 55%,rgba(20,18,50,0) 100%)}
.arrow-btn{position:absolute;top:230px;width:36px;height:36px;border:1px solid #ddd;border-radius:50%;display:flex;align-items:center;justify-content:center}
.arrow-btn.prev{left:58px}.arrow-btn.next{right:58px}

/* slogan */
.slogan{height:300px;background:var(--bg-dark);display:flex;justify-content:center;gap:0}
.slogan-item{width:352px;text-align:center;padding-top:52px}
.slogan-item svg{height:80px}
.slogan-item h3{font-family:"Montserrat",Arial,sans-serif;font-weight:400;font-size:22px;color:var(--violet);margin:26px 0 14px;text-shadow:0 0 8px #6a5cff}
.slogan-item p{font-size:12px;line-height:1.6;color:#e6e6e6;width:240px;margin:0 auto}

/* products */
.products{height:1235px;background:var(--bg)}
.products .neon-heading{padding-top:95px;font-size:40px}
.tabs{display:flex;justify-content:space-between;margin-top:70px}
.tab{width:106px;height:36px;border:1px solid #4a4a4a;font-size:11px;color:#aaa;display:flex;align-items:center;justify-content:center;border-radius:2px}
.grid{display:grid;grid-template-columns:repeat(3,297px);column-gap:24px;row-gap:26px;margin-top:63px}
.card{background:var(--card)}
.card .art{height:202px}
.card .info{height:126px;padding:26px 24px}
.card h4{font-family:"Montserrat",Arial,sans-serif;font-weight:700;font-size:13px;margin-bottom:12px}
.card p{font-size:11.5px;line-height:1.6;color:var(--muted)}
.more{text-align:center;margin-top:64px}

/* featured */
.featured{height:728px;background:linear-gradient(#1a1a1a,#141414)}
.featured .neon-heading{padding-top:95px;font-size:40px}
.feat-grid{display:flex;justify-content:center;gap:50px;margin-top:55px}
.feat-card{width:272px;background:var(--card-dark)}
.feat-card .art{height:196px}
.feat-card .info{height:168px;padding:28px 28px}
.feat-card h4{font-family:"Montserrat",Arial,sans-serif;font-weight:700;font-size:13px}
.price{font-family:"Montserrat",Arial,sans-serif;font-weight:700;font-size:24px;margin:8px 0 20px}
.feat-card .btn{font-size:11px;padding:8px 12px}
.dots{display:flex;justify-content:center;gap:12px;margin-top:64px}
.dots span{width:8px;height:8px;border-radius:50%;background:#888}
.dots span.on{background:#ddd}

/* promo */
.promo{height:547px;background:var(--bg-dark);position:relative;border-bottom:8px solid var(--orange)}
.promo-text{position:absolute;left:165px;top:165px;width:440px}
.promo-text h2{font-family:"Montserrat",Arial,sans-serif;font-weight:600;font-size:27px;line-height:1.3;color:var(--violet);text-transform:uppercase;margin-bottom:32px}
.promo-art{position:absolute;left:660px;top:40px;width:340px;height:499px;background:linear-gradient(160deg,#3a1c2c 0%,#1a1022 50%,#0b0b0b 100%)}

/* benefits */
.benefits{height:183px;background:var(--bg-panel);display:flex;justify-content:center}
.benefit{width:338px;display:flex;gap:22px;padding:48px 30px;border-right:1px solid var(--line)}
.benefit:last-child{border-right:none}
.benefit h5{font-family:"Montserrat",Arial,sans-serif;font-weight:700;font-size:13px;color:var(--violet);margin-bottom:6px}
.benefit p{font-size:11px;line-height:1.5;color:#ddd}

/* newsletter */
.newsletter{height:154px;background:var(--bg)}
.newsletter .wrap{height:154px;display:flex;align-items:center}
.newsletter h5{font-family:"Montserrat",Arial,sans-serif;font-weight:800;font-size:19px;line-height:1.1;color:var(--violet);width:170px;text-transform:uppercase}
.subscribe{width:385px;height:48px;background:var(--white);display:flex;align-items:center;border:2px solid #fff}
.subscribe span{flex:1;color:#333;font-size:12px;padding-left:16px;display:flex;gap:10px;align-items:center}
.subscribe b{background:var(--orange);height:100%;width:90px;display:flex;align-items:center;justify-content:center;font-family:"Montserrat",Arial,sans-serif;font-size:13px}
.follow{margin-left:auto;display:flex;align-items:center;gap:8px;font-family:"Montserrat",Arial,sans-serif;font-weight:700;font-size:11px}
.follow i{width:26px;height:26px;border-radius:50%;display:block}

/* footer */
.site-footer{height:364px;background:var(--bg-dark);position:relative}
.foot-cols{position:absolute;top:66px;left:0;display:flex}
.foot-col{width:260px;font-size:10.5px;color:#bbb;line-height:1.55}
.foot-col h6{font-family:"Montserrat",Arial,sans-serif;font-weight:700;font-size:11px;color:#fff;margin-bottom:10px}
.foot-col li{list-style:none}
.contact li{display:flex;gap:8px;margin-bottom:14px}
.foot-brand{position:absolute;left:0;top:250px;font-family:"Montserrat",Arial,sans-serif;font-weight:300;font-size:58px;color:var(--orange);text-transform:uppercase}
.copyright{position:absolute;right:0;top:286px;font-size:10px;color:#999}
</style>
</head>
<body>

<header class="site-header">
  <div class="wrap">
    <div class="brand">Brivaglo</div>
    <div class="utility">
      <div class="search">Search
        <svg width="12" height="12" viewBox="0 0 12 12"><circle cx="5" cy="5" r="3.5" stroke="#ddd" fill="none" stroke-width="1.5"/><line x1="7.5" y1="7.5" x2="11" y2="11" stroke="#ddd" stroke-width="1.5"/></svg>
      </div>
      <div class="call">
        <svg width="18" height="18" viewBox="0 0 24 24"><path d="M6 2l4 4-2 3c1 3 4 6 7 7l3-2 4 4-3 4C10 21 3 14 2 5z" fill="#fff"/></svg>
        <div><small>CALL US</small>512.555.0142</div>
      </div>
      <div class="login">
        <svg width="10" height="12" viewBox="0 0 10 12"><rect x="1" y="5" width="8" height="7" fill="#fff"/><path d="M3 5V3a2 2 0 014 0v2" stroke="#fff" fill="none"/></svg>Login
      </div>
      <div class="cart">MY CART
        <svg width="18" height="16" viewBox="0 0 18 16"><path d="M1 1h3l2 9h9l2-6H5" stroke="#fff" fill="none" stroke-width="1.5"/><circle cx="7" cy="14" r="1.5" fill="#fff"/><circle cx="14" cy="14" r="1.5" fill="#fff"/></svg>
        <span class="count">0</span>
      </div>
    </div>
    <nav class="main-nav">
      <a class="active" href="#">HOME</a><a href="#">ABOUT US</a><a href="#">PRODUCTS</a><a href="#">SERVICES</a><a href="#">BLOG</a><a href="#">CONTACT US</a>
    </nav>
  </div>
</header>

<section class="hero">
  <h1 class="neon-heading hero-title">LED EDGE LIT SIGNS</h1>
  <div class="hero-art" role="img" aria-label="Glowing purple-framed edge lit neon sign on a dark brick wall"></div>
  <div class="arrow-btn prev"><svg width="10" height="10" viewBox="0 0 10 10"><path d="M7 1L3 5l4 4" stroke="#fff" fill="none" stroke-width="1.5"/></svg></div>
  <div class="arrow-btn next"><svg width="10" height="10" viewBox="0 0 10 10"><path d="M3 1l4 4-4 4" stroke="#fff" fill="none" stroke-width="1.5"/></svg></div>
</section>

<section class="slogan">
  <div class="slogan-item">
    <svg viewBox="0 0 60 80" width="60"><path d="M10 14h36l8 8-8 8H10z" fill="var(--orange)"/><path d="M50 38H18l-8 8 8 8h32z" fill="var(--orange)"/><rect x="27" y="8" width="6" height="70" fill="var(--orange)"/></svg>
    <h3>CREATE</h3>
    <p>Lorem Ipsum is simply dummy text of the printing and typesetting industry.</p>
  </div>
  <div class="slogan-item">
    <svg viewBox="0 0 60 80" width="60"><rect x="27" y="0" width="6" height="18" fill="#ddd"/><path d="M18 18h24v14l6 22H12l6-22z" fill="var(--orange)"/><circle cx="30" cy="60" r="7" fill="#fff"/><path d="M8 66l-6 6M52 66l6 6M30 70v8" stroke="var(--orange)" stroke-width="3"/></svg>
    <h3>ENERGIZE</h3>
    <p>Lorem Ipsum is simply dummy text of the printing and typesetting industry.</p>
  </div>
  <div class="slogan-item">
    <svg viewBox="0 0 100 80" width="100"><rect x="6" y="14" width="88" height="52" rx="6" fill="none" stroke="var(--orange)" stroke-width="5"/><text x="50" y="50" text-anchor="middle" font-family="Montserrat,Arial,sans-serif" font-weight="700" font-size="24" fill="none" stroke="var(--orange)" stroke-width="2">LED</text></svg>
    <h3>AMAZE</h3>
    <p>Lorem Ipsum is simply dummy text of the printing and typesetting industry.</p>
  </div>
</section>

<section class="products">
  <div class="wrap">
    <h2 class="neon-heading">OUR PRODUCTS</h2>
    <div class="tabs">
      <div class="tab">Heading 1</div><div class="tab">Heading 2</div><div class="tab">Heading 3</div><div class="tab">Heading 4</div><div class="tab">Heading 5</div><div class="tab">Heading 6</div><div class="tab">Heading 7</div><div class="tab">Heading 8</div>
    </div>
    <div class="grid">
      <article class="card"><div class="art" role="img" aria-label="Neon pizzeria sign with pizza slice" style="background:linear-gradient(135deg,#1c2a6b,#b0203a)"></div><div class="info"><h4>LOREM IPSUM IS SIMPLY</h4><p>Lorem Ipsum is simply dummy text of the printing and typesetting industry.</p></div></article>
      <article class="card"><div class="art" role="img" aria-label="Vintage city marquee neon sign" style="background:linear-gradient(135deg,#2a0c08,#8a2a10)"></div><div class="info"><h4>LOREM IPSUM IS SIMPLY</h4><p>Lorem Ipsum is simply dummy text of the printing and typesetting industry.</p></div></article>
      <article class="card"><div class="art" role="img" aria-label="Red script neon sign on a dark wall" style="background:radial-gradient(circle,#5a1016,#120606)"></div><div class="info"><h4>LOREM IPSUM IS SIMPLY</h4><p>Lorem Ipsum is simply dummy text of the printing and typesetting industry.</p></div></article>
      <article class="card"><div class="art" role="img" aria-label="Green hotel neon sign at night" style="background:linear-gradient(135deg,#0d3a34,#3a1230)"></div><div class="info"><h4>LOREM IPSUM IS SIMPLY</h4><p>Lorem Ipsum is simply dummy text of the printing and typesetting industry.</p></div></article>
      <article class="card"><div class="art" role="img" aria-label="Guitar and live music neon sign" style="background:linear-gradient(135deg,#1e1e1e,#3c3c3c)"></div><div class="info"><h4>LOREM IPSUM IS SIMPLY</h4><p>Lorem Ipsum is simply dummy text of the printing and typesetting industry.</p></div></article>
      <article class="card"><div class="art" role="img" aria-label="Retro movie night neon sign" style="background:linear-gradient(135deg,#0f3a3a,#6a2a12)"></div><div class="info"><h4>LOREM IPSUM IS SIMPLY</h4><p>Lorem Ipsum is simply dummy text of the printing and typesetting industry.</p></div></article>
    </div>
    <div class="more"><span class="btn">VIEW MORE PRODUCTS</span></div>
  </div>
</section>

<section class="featured">
  <h2 class="neon-heading">FEATURED PRODUCTS</h2>
  <div class="feat-grid">
    <article class="feat-card"><div class="art" role="img" aria-label="Green neon tree sign with stars" style="background:linear-gradient(135deg,#0a0a0a,#1b3a1b)"></div><div class="info"><h4>LOREM IPSUM IS SIMPLY</h4><div class="price">$15.99</div><span class="btn">ADD TO CART</span></div></article>
    <article class="feat-card"><div class="art" role="img" aria-label="Blue and yellow LED diode neon sign" style="background:linear-gradient(135deg,#0e1a4a,#4a3a0a)"></div><div class="info"><h4>LOREM IPSUM IS SIMPLY</h4><div class="price">$15.99</div><span class="btn">ADD TO CART</span></div></article>
    <article class="feat-card"><div class="art" role="img" aria-label="Bar neon sign with bottle on brick" style="background:linear-gradient(135deg,#2e3a2a,#4a4a4a)"></div><div class="info"><h4>LOREM IPSUM IS SIMPLY</h4><div class="price">$15.99</div><span class="btn">ADD TO CART</span></div></article>
  </div>
  <div class="dots"><span></span><span></span><span class="on"></span><span></span></div>
</section>

<section class="promo">
  <div class="promo-text">
    <h2>Lorem Ipsum is simply dummy text of the printing and typesetting industry.</h2>
    <span class="btn">SHOW ALL COLLECTIONS</span>
  </div>
  <div class="promo-art" role="img" aria-label="Tall vintage motel neon sign glowing at night"></div>
</section>

<section class="benefits">
  <div class="benefit">
    <svg width="50" height="40" viewBox="0 0 50 40"><rect x="2" y="8" width="28" height="20" fill="var(--orange)"/><path d="M30 14h10l8 8v6H30z" fill="var(--orange)"/><circle cx="12" cy="31" r="5" fill="#fff"/><circle cx="40" cy="31" r="5" fill="#fff"/></svg>
    <div><h5>FREE SHIPPING</h5><p>Lorem ipsum dolor sit amet cons ectetur adipiscing elit</p></div>
  </div>
  <div class="benefit">
    <svg width="44" height="40" viewBox="0 0 44 40"><rect x="2" y="18" width="9" height="20" fill="var(--orange)"/><path d="M14 18l8-14c4 0 5 3 4 7l-2 6h14c3 0 4 3 3 5l-5 14H14z" fill="var(--orange)"/></svg>
    <div><h5>QUALITY PRODUCTS</h5><p>Lorem ipsum dolor sit amet cons ectetur adipiscing elit</p></div>
  </div>
  <div class="benefit">
    <svg width="44" height="44" viewBox="0 0 44 44"><circle cx="22" cy="22" r="18" fill="none" stroke="var(--orange)" stroke-width="4"/><text x="22" y="30" text-anchor="middle" font-family="Montserrat,Arial,sans-serif" font-weight="700" font-size="22" fill="var(--orange)">$</text></svg>
    <div><h5>MONEY BACK GUARANTEE</h5><p>Lorem ipsum dolor sit amet cons ectetur adipiscing elit</p></div>
  </div>
</section>

<section class="newsletter">
  <div class="wrap">
    <h5>Newsletter Subscribe</h5>
    <div class="subscribe">
      <span><svg width="14" height="10" viewBox="0 0 14 10"><rect x=".5" y=".5" width="13" height="9" fill="none" stroke="#555"/><path d="M1 1l6 5 6-5" stroke="#555" fill="none"/></svg>E mail id</span>
      <b>SIGNUP</b>
    </div>
    <div class="follow">FOLLOW :
      <i style="background:#3b5bb5"></i><i style="background:#2aa3e0"></i><i style="background:#2f6f9a"></i><i style="background:#d8282f"></i>
    </div>
  </div>
</section>

<footer class="site-footer">
  <div class="wrap">
    <div class="foot-cols">
      <ul class="foot-col"><h6>HELP</h6><li>Contact Us</li><li>Shopping FAQs</li><li>Shipping &amp; Delivery</li><li>Returns &amp; Exchanges</li><li>Privacy &amp; Security</li></ul>
      <ul class="foot-col"><h6>MY ACCOUNT</h6><li>Login</li><li>Register</li><li>My Cart</li><li>My Wishlist</li><li>FAQ</li></ul>
      <ul class="foot-col" style="width:225px"><h6>MENU</h6><li>Home</li><li>About Us</li><li>Products</li><li>Services</li><li>Blog</li><li>Contact Us</li></ul>
      <ul class="foot-col contact" style="width:200px"><h6>CONTACT US</h6>
        <li><svg width="10" height="12" viewBox="0 0 10 12"><path d="M5 12S1 7 1 4.5a4 4 0 018 0C9 7 5 12 5 12z" fill="#bbb"/></svg>1208 Lantern Ave, Austin, Texas 78701 United States</li>
        <li><svg width="10" height="10" viewBox="0 0 24 24"><path d="M6 2l4 4-2 3c1 3 4 6 7 7l3-2 4 4-3 4C10 21 3 14 2 5z" fill="#bbb"/></svg>512.555.0142</li>
        <li><svg width="12" height="9" viewBox="0 0 14 10"><rect width="14" height="10" fill="#bbb"/><path d="M0 0l7 6 7-6" stroke="#0b0b0b" fill="none"/></svg>info@brivaglo.com</li>
      </ul>
    </div>
    <div class="foot-brand">Brivaglo</div>
    <div class="copyright">Copyright © 2018 All Rights Reserved</div>
  </div>
</footer>

</body>
</html>
```